Certified Legal Nurse Consultant business needs a postcard design

Need a postcard that advertises to target market of attorneys. I am a registered nurse who helps lawyers with the medical issues on their cases. I want this card to highlight the benefit of my services versus the competition. Please see attached document for more info.
Updates

Reason: Many of the 20 designs I received were from the same designer, but just altered slightly. I was expecting ~20 original/unique designs. Thanks!

Target Market(s)

attorneys (lawyers)

Industry/Entity Type

Business

Font styles to use
Serif

Colors
3176b5
0355a3

Requirements
Must have
• my photo, business name and address, phone number, web address, description of how my business is better than the competition (see PDF file sent)

```html
<!DOCTYPE html>
<html lang="en">
<head>
<meta charset="utf-8">
<title>M. Haverland &amp; Associates LLC – Legal Nurse Consulting</title>
<link rel="stylesheet" href="https://fonts.googleapis.com/css2?family=PT+Sans:wght@700&family=Roboto+Condensed:wght@400;700&display=swap">
<style>
  :root {
    --page: #ecebe8;
    --blue-deep: #0355a3;
    --blue-mid: #3176b5;
    --blue-soft: #6fa6dd;
    --blue-glow: #b4d6f4;
    --stripe: #e6ecf2;
    --ink-navy: #0b1d3a;
    --white: #ffffff;
  }
  * { box-sizing: border-box; margin: 0; padding: 0; }
  html, body {
    width: 900px; height: 1200px; overflow: hidden;
    background: var(--page);
  }
  .flyer {
    position: absolute; left: 160px; top: 30px;
    width: 570px; height: 1140px; overflow: hidden;
    background:
      radial-gradient(ellipse 60% 45% at 70% 28%, var(--blue-glow) 0%, rgba(180,214,244,0) 100%),
      radial-gradient(ellipse 55% 35% at 40% 68%, rgba(180,214,244,.8) 0%, rgba(180,214,244,0) 100%),
      linear-gradient(180deg, var(--blue-soft) 0%, #5d97d4 40%, #6ca5df 70%, var(--blue-mid) 100%);
    color: var(--white);
    font-family: "Roboto Condensed", "Arial Narrow", sans-serif;
  }
  .stripe { position: absolute; left: 0; width: 100%; background: var(--stripe); }
  .title-bar {
    position: absolute; left: 0; top: 40px; width: 100%; height: 46px;
    background: linear-gradient(90deg, #4c8bcd, #7bb2e6 60%, #4c8bcd);
    text-align: center;
    font-family: "PT Sans", sans-serif; font-weight: 700;
    font-size: 29px; line-height: 46px; color: var(--white);
  }
  .tab {
    position: absolute; left: 0;
    background: linear-gradient(180deg, #1a67b6, var(--blue-deep));
    border-radius: 0 14px 14px 0;
    box-shadow: 0 4px 6px rgba(0,40,90,.45);
    font-weight: 700; color: var(--white);
  }
  .tab--question {
    top: 148px; width: 523px; height: 90px;
    padding: 12px 0 0 24px; font-size: 28px; line-height: 31px;
  }
  .tab--contact {
    top: 596px; width: 276px; height: 90px;
    padding: 18px 0 0 32px; font-size: 42px; line-height: 50px;
  }
  .benefits {
    position: absolute; left: 14px; top: 258px; width: 550px;
    list-style: none; font-size: 16.4px; line-height: 18.5px;
  }
  .benefits li { position: relative; padding-left: 16px; margin-bottom: 13px; }
  .benefits li::before {
    content: ""; position: absolute; left: 0; top: 5px;
    width: 10px; height: 10px; border-radius: 50%; background: #0a0f1a;
  }
  .benefits li.gap { margin-bottom: 20px; }
  .contact-line {
    position: absolute; left: 14px; display: flex; align-items: flex-start;
    font-size: 18px; line-height: 20px; color: var(--white);
  }
  .contact-line svg { flex: none; margin-right: 6px; margin-top: 3px; }
  .contact-line--phone { top: 710px; font-size: 20px; }
  .contact-line--address { top: 755px; }
  .contact-line--email { top: 831px; font-size: 15.5px; }
  .portrait {
    position: absolute; left: 252px; top: 708px;
    width: 316px; height: 316px; border-radius: 50%;
    border: 7px solid var(--white);
    background: radial-gradient(circle at 50% 45%, #8a6a5c 0%, #4a3a36 45%, #1a1a1e 100%);
    box-shadow: 0 3px 8px rgba(0,0,0,.35);
  }
  .contact-person {
    position: absolute; left: 22px; top: 894px;
    font-size: 32px; font-weight: 700; color: var(--ink-navy);
    text-shadow: 0 1px 1px rgba(255,255,255,.4);
  }
  .consultant {
    position: absolute; left: 22px; top: 956px;
    font-size: 32px; line-height: 38px; font-weight: 700; color: var(--white);
    text-shadow: 1px 2px 2px rgba(0,20,50,.8);
  }
  .footer {
    position: absolute; left: 0; top: 1073px; width: 100%; height: 40px;
    background: linear-gradient(180deg, #f0f4f8, #cfdbe7);
    text-align: center; font-family: "PT Sans", sans-serif; font-weight: 700;
    font-size: 25px; line-height: 40px; color: var(--ink-navy);
  }
</style>
</head>
<body>
<main class="flyer">
  <div class="stripe" style="top:10px;height:9px"></div>
  <div class="stripe" style="top:25px;height:9px"></div>
  <div class="title-bar">M. Haverland &amp; Associates LLC</div>
  <div class="stripe" style="top:90px;height:10px"></div>
  <div class="stripe" style="top:108px;height:10px"></div>

  <h2 class="tab tab--question">What makes your product/service better<br>than the guys down the street?</h2>

  <ul class="benefits">
    <li>Currently active as a Registered Nurse in the case management<br>of patients with injuries and illnesses. My experience and certification<br>provides attorneys with an RN that has upto date knowledge of practices,<br>policies, procedures, as well as long term patient needs and associated<br>costs</li>
    <li class="gap">Length and breadth of experience. As a masters prepared RN,<br>my 26 years of nursing background includes work in virtually every<br>health care setting including hospital, home care, skilled nursing facility,<br>clinical research and outpatient case management.During this time,<br>I have reviewed, critiqued, and summarized thousands of medical records</li>
    <li>RN-licensed in 14 states (MN, CA, AZ, WA, WY, TX, IA, GA, MS, CT,<br>OH, NV, SD, OK)</li>
    <li>Published in peer-reviewed medical and nursing journals,<br>including first authorship</li>
  </ul>

  <h2 class="tab tab--contact">Contact Us</h2>

  <p class="contact-line contact-line--phone">
    <svg width="14" height="14" viewBox="0 0 24 24" aria-hidden="true"><path fill="#0a0f1a" d="M6.6 10.8a15.1 15.1 0 0 0 6.6 6.6l2.2-2.2c.3-.3.7-.4 1-.2 1.1.4 2.3.6 3.6.6.6 0 1 .4 1 1V20c0 .6-.4 1-1 1A17 17 0 0 1 3 4c0-.6.4-1 1-1h3.5c.6 0 1 .4 1 1 0 1.3.2 2.5.6 3.6.1.3 0 .7-.2 1z"/></svg>
    (555) 014 2278
  </p>
  <p class="contact-line contact-line--address">
    <svg width="14" height="14" viewBox="0 0 24 24" aria-hidden="true"><path fill="#0a0f1a" d="M12 3 2 12h3v8h5v-6h4v6h5v-8h3z"/></svg>
    <span>M. Haverland &amp; Associates<br>LLC 1820 Meadowlark Lane<br>Cedar Grove, MN 55000</span>
  </p>
  <p class="contact-line contact-line--email">
    <svg width="11" height="11" viewBox="0 0 12 12" aria-hidden="true"><circle cx="6" cy="6" r="5" fill="#2a3b55"/></svg>
    dana@haverland-associates.com
  </p>

  <div class="portrait" role="img" aria-label="Portrait photo of Dana Haverland, the consultant"></div>

  <p class="contact-person">Contact Person</p>
  <p class="consultant">Dana Haverland<br>legal nurse consulting</p>

  <div class="stripe" style="top:1062px;height:8px"></div>
  <div class="footer">www.haverlandassociates.com</div>
  <div class="stripe" style="top:1117px;height:6px"></div>
</main>
</body>
</html>
```